New modern business card design

To design a brand new business card that's clean & modern in terms of layout.
I have attached our company logo and also basic information regarding what is needed on the card that also needs to be editable.

Target Market(s)

motor trade

Contact Information for Business Card

logo, name, title, tel, mob, email, address, www, all information is in the word.doc file

Requirements
Must have
• white background
Nice to have
• Nice clean font

```html
<!DOCTYPE html>
<html lang="en">
<head>
<meta charset="utf-8">
<title>Bolt Works Ltd – Business Card</title>
<link rel="stylesheet" href="https://fonts.googleapis.com/css2?family=Mulish:wght@400;600;700&display=swap">
<style>
  :root {
    --backdrop: #6aa5cb;
    --card: #ffffff;
    --brand-blue: #1a73bb;
    --text-grey: #8b8b8b;
    --mark-grey: #a7a7a7;
  }
  html, body {
    margin: 0;
    width: 1200px;
    height: 1200px;
    overflow: hidden;
    background: var(--backdrop);
    font-family: "Mulish", Arial, sans-serif;
  }
  .business-card {
    position: absolute;
    left: 100px;
    top: 314px;
    width: 1000px;
    height: 571px;
    background: var(--card);
    box-shadow: 0 18px 40px rgba(20, 50, 80, 0.25);
  }
  .holder { position: absolute; left: 60px; top: 50px; }
  .holder-name {
    margin: 0;
    font-size: 46px;
    font-weight: 400;
    color: var(--text-grey);
    line-height: 1.1;
    letter-spacing: 0.3px;
  }
  .holder-name .surname { color: var(--brand-blue); font-weight: 700; }
  .holder-title {
    margin: 2px 0 0;
    font-size: 25px;
    color: var(--brand-blue);
    font-weight: 400;
  }
  .brand-corner {
    position: absolute;
    right: 59px;
    top: 56px;
    display: flex;
    align-items: center;
    gap: 10px;
    font-size: 30px;
    font-weight: 700;
    color: var(--brand-blue);
  }
  .brand-corner .brand-square {
    width: 22px; height: 22px; background: var(--mark-grey);
  }
  .contact-list {
    position: absolute;
    left: 60px;
    top: 252px;
    margin: 0;
    padding: 0;
    list-style: none;
    font-size: 25px;
    color: var(--text-grey);
    line-height: 33px;
  }
  .contact-list li {
    display: flex;
    align-items: flex-start;
    margin-bottom: 7px;
  }
  .contact-list .icon {
    width: 18px; height: 18px;
    margin: 8px 14px 0 0;
    flex: none;
    fill: var(--brand-blue);
  }
  .brand-foot {
    position: absolute;
    right: 59px;
    bottom: 58px;
    font-size: 38px;
    font-weight: 700;
    color: var(--brand-blue);
    letter-spacing: 1px;
  }
</style>
</head>
<body>
  <section class="business-card">
    <header class="holder">
      <h1 class="holder-name">Daniel <span class="surname">Marsh</span></h1>
      <p class="holder-title">General Manager</p>
    </header>

    <div class="brand-corner"><span class="brand-square"></span>Bolt Works</div>

    <ul class="contact-list">
      <li>
        <svg class="icon" viewBox="0 0 18 18"><path d="M5 0h8a2 2 0 0 1 2 2v14a2 2 0 0 1-2 2H5a2 2 0 0 1-2-2V2a2 2 0 0 1 2-2zm0 2v12h8V2zm4 13a1 1 0 1 0 0 2 1 1 0 0 0 0-2z"/></svg>
        0161 555 0182
      </li>
      <li>
        <svg class="icon" viewBox="0 0 18 18"><rect width="18" height="18" rx="3"/><path fill="#fff" d="M5 4l2 0 1 3-1.3 1a7 7 0 0 0 3.3 3.3L11 10l3 1v2a1 1 0 0 1-1 1A9 9 0 0 1 4 5a1 1 0 0 1 1-1z"/></svg>
        07700 900 461
      </li>
      <li>
        <svg class="icon" viewBox="0 0 18 18"><rect width="18" height="18" rx="3"/><rect x="4" y="5" width="10" height="8" fill="#fff"/><path d="M4 5l5 4 5-4" fill="none" stroke="#1a73bb" stroke-width="1.5"/></svg>
        dmarsh@boltworks.co.uk
      </li>
      <li>
        <svg class="icon" viewBox="0 0 18 18"><path d="M9 0a6 6 0 0 1 6 6c0 4.5-6 12-6 12S3 10.5 3 6a6 6 0 0 1 6-6zm0 3.5a2.5 2.5 0 1 0 0 5 2.5 2.5 0 0 0 0-5z"/></svg>
        <span>Foundry Lane<br>Ashbrook, Manchester<br>M99 2QT</span>
      </li>
      <li>
        <svg class="icon" viewBox="0 0 18 18"><circle cx="9" cy="9" r="9"/><path fill="#fff" d="M5 4c2 1 3 3 2 5s-3 1-3 4c-1-1-2-3-2-4 0-2 1-4 3-5zm7 8c1-2 3-2 4-1-1 3-3 5-6 5 1-1 1-3 2-4z"/></svg>
        www.boltworks.co.uk
      </li>
    </ul>

    <div class="brand-foot">Bolt Works Ltd</div>
  </section>
</body>
</html>
```